" UNFADING SPRINGTIDE 2020 ".

I want a flyer to invite people to a 2 Days Miracle Service. Salvation, Deliverance, Healing, Restoration, Breakthrough .
The best flyer you can propose me. Insert the logo i send you on the flyer. 04/11-04/12/2020. From 6:00Pm-10:00Pm. Venue: 5:00Pm. With Evangelist PAUL-HENRI MADOLEBA. ( LAMP & RIVER Ministry ) At: Tenbury Fellowship Hall. 24730 PELDRA Street, Romulus, Michigan 48174. Jesus-Christ Is the Lord.
Contact: - email : lampriverfel@outlook-mail.example
- cell phone: 5550419826
- Whatsapp :5550419826

Target Market(s)

Michigan, all ages

Font styles to use
Decorative
Script

Requirements
Must have
• Must have the logo of the ministry.

```html
<!DOCTYPE html>
<html lang="en">
<head>
<meta charset="utf-8">
<title>Unfading Springtide 2020 – Evangelic Services</title>
<link rel="stylesheet" href="https://fonts.googleapis.com/css2?family=Alfa+Slab+One&family=Roboto:wght@700;900&family=Roboto+Slab:wght@800&display=swap">
<style>
  :root {
    --stage: #737373;
    --paper: #f2eeec;
    --night: #3b3a36;
    --pink: #e8327c;
    --cyan: #55b9c2;
    --blue: #2f6aaa;
    --red: #e84437;
    --banner: #6b8fc5;
    --gold: #f5c518;
    --ink: #161616;
    --white: #ffffff;
    --mark: #4f86c6;
  }
  * { box-sizing: border-box; margin: 0; padding: 0; }
  html, body { width: 1200px; height: 1200px; overflow: hidden; background: var(--stage); }
  .flyer {
    position: absolute; left: 302px; top: 117px;
    width: 595px; height: 840px;
    background: var(--paper); overflow: hidden;
  }
  .flyer-shapes { position: absolute; inset: 0; width: 100%; height: 100%; }
  .ministry-mark {
    position: absolute; left: 49px; top: 26px;
    width: 274px; height: 274px; border-radius: 50%;
    background: radial-gradient(circle at 40% 40%, #e9f3f6 0%, #7fb3d8 55%, var(--mark) 100%);
  }
  .ministry-name {
    position: absolute; left: 0; width: 360px; text-align: center;
    font-family: "Roboto", sans-serif; font-weight: 900; color: var(--red);
    line-height: 1;
  }
  .ministry-name--main { top: 348px; font-size: 28px; }
  .ministry-name--sub { top: 381px; font-size: 23px; }
  .speaker-title {
    position: absolute; left: 170px; width: 300px; top: 461px; text-align: center;
    font-family: "Alfa Slab One", serif; font-size: 34px; color: var(--gold);
    letter-spacing: 1px; line-height: 1;
  }
  .speaker-name {
    position: absolute; left: 160px; width: 320px; top: 506px; text-align: center;
    font-family: "Roboto Slab", serif; font-weight: 800; font-size: 20px; color: var(--white);
    letter-spacing: 1px; line-height: 1;
  }
  .service-intro, .service-themes {
    position: absolute; left: 0; width: 100%; text-align: center;
    font-family: "Roboto", sans-serif; font-weight: 700; color: var(--ink);
    font-size: 17px; line-height: 23px;
  }
  .service-intro { top: 577px; left: 0; padding-left: 0; }
  .service-themes { top: 622px; padding: 0 8px; }
  .event-details {
    position: absolute; left: 12px; top: 755px;
    font-family: "Roboto Slab", serif; font-weight: 800; font-size: 10.5px;
    letter-spacing: 1px; line-height: 14.4px; color: var(--ink); list-style: none;
  }
  .event-details .indent { padding-left: 38px; }
</style>
</head>
<body>
  <main class="flyer">
    <svg class="flyer-shapes" viewBox="0 0 958 1352" preserveAspectRatio="none" aria-hidden="true">
      <path class="speaker-banner" fill="var(--banner)" d="M253 600 H748 V857 L500 904 L253 857 Z"/>
      <path class="wave wave-red" fill="var(--red)" d="M0 0 H958 V680 C880 610,760 600,600 650 C400 715,250 800,110 788 C60 784,20 770,0 755 Z"/>
      <path class="wave wave-blue" fill="var(--blue)" d="M0 0 H958 V632 C870 585,760 585,620 625 C430 680,280 760,140 745 C80 738,30 725,0 705 Z"/>
      <path class="wave wave-cyan" fill="var(--cyan)" d="M0 0 H958 V605 C870 570,760 570,640 600 C450 650,300 740,150 720 C90 712,40 700,0 680 Z"/>
      <path class="wave wave-pink" fill="var(--pink)" d="M0 0 H958 V595 C870 555,760 550,640 580 C450 630,300 710,150 700 C90 696,40 682,0 655 Z"/>
      <path class="wave wave-night" fill="var(--night)" d="M0 0 H958 V585 C870 545,760 540,640 570 C450 620,300 700,150 690 C90 686,40 672,0 645 Z"/>
      <path class="footer-band" fill="var(--blue)" d="M0 1310 H581 L696 1265 H958 V1352 H0 Z"/>
    </svg>

    <div class="ministry-mark" role="img" aria-label="Ministry emblem"></div>
    <p class="ministry-name ministry-name--main">LAMP &amp; RIVER</p>
    <p class="ministry-name ministry-name--sub">Ministries</p>

    <h1 class="speaker-title">EVANGELIST</h1>
    <h2 class="speaker-name">PAUL-HENRI MADOLEBA</h2>

    <p class="service-intro">2 DAYS EVANGELIC SERVICES OF</p>
    <p class="service-themes">SALVATION, DELIVERANCE, HEALING, RESTORATION, BLESSINGS<br>AND FINANCIAL BREAKTHROUGH</p>

    <ul class="event-details">
      <li>DATE: 04/11-04/12/2020</li>
      <li>TIME: 6:00PM-10:00PM</li>
      <li>VENUE:TENBURY FELLOWSHIP HALL.</li>
      <li class="indent">24730 PELDRA STREET, ROMULUS, MICHIGAN 48174</li>
    </ul>
  </main>
</body>
</html>
```